Virgin Coconut Oil Label

Need to update label to a newer design using all the same information. Our company manufactures Coconut Products.
Target Market(s)
Pharmacies, dept stores, groceries.
Look and feel
Each slider illustrates characteristics of the customer's brand and the style your logo design should communicate.

```html
<!DOCTYPE html>
<html lang="en">
<head>
<meta charset="utf-8">
<title>Isla Grove Virgin Coconut Oil Label</title>
<link rel="stylesheet" href="https://fonts.googleapis.com/css2?family=Antonio:wght@200;300;400;500;700&display=swap">
<style>
  :root {
    --bg: #e4e4e4;
    --label: #ffffff;
    --brown: #6b3a1e;
    --brown-soft: #8a5a36;
    --green: #5b9a2a;
    --green-dark: #3f7a1c;
    --leaf-light: #e6f0da;
    --leaf: #a9cb8b;
    --photo-cream: #f1ebdf;
    --photo-green: #b9d3a0;
    --badge: #2f6b2a;
    --eu: #7cb82f;
  }
  html, body {
    margin: 0;
    padding: 0;
    width: 1200px;
    height: 1134px;
    overflow: hidden;
    background: var(--bg);
    font-family: "Antonio", sans-serif;
  }
  .label {
    position: absolute;
    left: 302px;
    top: 40px;
    width: 595px;
    height: 1054px;
    background: var(--label);
    overflow: hidden;
    box-shadow: 0 6px 24px rgba(0,0,0,0.12);
  }
  .palm-leaf {
    position: absolute;
    left: 352px;
    top: 0;
    width: 243px;
    height: 578px;
    background: linear-gradient(200deg, var(--leaf) 0%, var(--leaf-light) 60%, rgba(255,255,255,0) 100%);
  }
  .coconut-photo {
    position: absolute;
    left: 194px;
    top: 561px;
    width: 401px;
    height: 493px;
    background: linear-gradient(160deg, var(--photo-cream) 0%, #f6f2ea 55%, var(--photo-green) 100%);
  }
  .brand {
    position: absolute;
    left: 0;
    top: 170px;
    width: 595px;
    display: flex;
    align-items: center;
    justify-content: center;
    gap: 14px;
  }
  .brand-dot {
    width: 34px;
    height: 34px;
    border-radius: 50%;
    background: var(--green);
  }
  .brand-name {
    font-weight: 500;
    font-size: 46px;
    letter-spacing: 5px;
    color: var(--brown);
  }
  .product-name {
    position: absolute;
    left: 22px;
    top: 372px;
    margin: 0;
    font-weight: 700;
    font-size: 122px;
    line-height: 1;
    color: var(--brown);
    white-space: nowrap;
  }
  .rule {
    position: absolute;
    left: 22px;
    top: 502px;
    width: 447px;
    height: 7px;
    background: var(--brown);
  }
  .origin {
    position: absolute;
    left: 279px;
    top: 520px;
    font-weight: 400;
    font-size: 20px;
    color: var(--brown-soft);
    white-space: nowrap;
  }
  .badge-organic {
    position: absolute;
    left: 505px;
    top: 505px;
    width: 62px;
    height: 62px;
    border-radius: 50%;
    background: var(--label);
    border: 5px solid var(--badge);
  }
  .badge-eu {
    position: absolute;
    left: 512px;
    top: 940px;
    width: 75px;
    height: 75px;
    background: var(--eu);
  }
  .claims {
    position: absolute;
    left: 20px;
    top: 530px;
    width: 190px;
    line-height: 1;
    white-space: nowrap;
  }
  .claims span { display: block; }
  .claim-percent { font-weight: 200; font-size: 96px; color: var(--green); }
  .claim-natural { font-weight: 700; font-size: 56px; color: var(--green); margin-top: 4px; }
  .claim-extra { font-weight: 300; font-size: 78px; color: var(--brown); margin-top: 4px; }
  .claim-organic { font-weight: 300; font-size: 60px; color: var(--green); margin-top: 4px; }
  .claim-virgin { font-weight: 700; font-size: 72px; color: var(--brown); margin-top: 4px; }
  .claim-cold { font-weight: 300; font-size: 38px; color: var(--green); margin-top: 2px; }
  .claim-supplement {
    font-weight: 400;
    font-size: 26px;
    color: #fff;
    background: var(--green-dark);
    padding: 2px 6px;
    margin-top: 6px;
    width: max-content;
  }
  .claim-mct { font-weight: 400; font-size: 17px; color: var(--brown); margin-top: 8px; }
</style>
</head>
<body>
  <main class="label">
    <div class="palm-leaf" role="img" aria-label="Green palm frond illustration"></div>
    <div class="coconut-photo" role="img" aria-label="Photo of a halved coconut on green leaves"></div>

    <div class="brand">
      <span class="brand-dot"></span>
      <span class="brand-name">ISLA GROVE</span>
    </div>

    <h1 class="product-name">COCONUT OIL</h1>
    <div class="rule"></div>
    <div class="origin">PRODUCT OF PHILIPPINES</div>
    <div class="badge-organic" role="img" aria-label="Organic certification badge"></div>

    <div class="claims">
      <span class="claim-percent">100%</span>
      <span class="claim-natural">NATURAL</span>
      <span class="claim-extra">EXTRA</span>
      <span class="claim-organic">ORGANIC</span>
      <span class="claim-virgin">VIRGIN</span>
      <span class="claim-cold">COLD PRESSED</span>
      <span class="claim-supplement">DIETARY SUPPLEMENT</span>
      <span class="claim-mct">CONTAINS MCT</span>
    </div>

    <div class="badge-eu" role="img" aria-label="Organic certification mark"></div>
  </main>
</body>
</html>
```